Career Development Skills | Business Card & Logo Design

We are looking for a business card including logo design for a new Sydney based business called 'Bright Pathway'.
We offer a range of services that focus on building the Employability or Employment skills for individuals focusing on job seekers and those interested in building skills required to develop their career. Employability skills are required not only to gain employment, but also to progress within an organisation so as to achieve one's potential.
Target Market(s)
Our client targets include corporates and govt agencies looking to build skills within their current employee base or assist staff in the transition between roles or workplaces.
Industry/Entity Type
Business
Look and feel
Each slider illustrates characteristics of the customer's brand and the style your logo design should communicate.

```html
<!DOCTYPE html>
<html lang="en">
<head>
<meta charset="utf-8">
<title>Bright Pathway – Business Card</title>
<link href="https://fonts.googleapis.com/css2?family=Cinzel:wght@700&family=Pathway+Gothic+One&display=swap" rel="stylesheet">
<style>
  :root {
    --backdrop: #1b1b1d;
    --card-navy: #06107a;
    --card-white: #ffffff;
    --rule-light: #8d93c9;
    --ink-navy: #1d2a8a;
    --ink-grey: #5a5f63;
    --silver-start: #c3cfcc;
    --silver-end: #f6f5f8;
  }
  * { margin: 0; padding: 0; box-sizing: border-box; }
  html, body {
    width: 1200px; height: 1164px; overflow: hidden;
    background: var(--backdrop);
  }
  .canvas { position: relative; width: 1200px; height: 1164px; }

  .card { position: absolute; box-shadow: 0 6px 18px rgba(0,0,0,.55); }

  /* Front */
  .card-front {
    left: 143px; top: 89px; width: 708px; height: 433px;
    background: var(--card-navy);
  }
  .brand-rule {
    position: absolute; left: 151px; top: 244px; width: 413px; height: 1px;
    background: linear-gradient(90deg, transparent, var(--rule-light) 15%, var(--rule-light) 85%, transparent);
  }
  .brand-name {
    position: absolute; left: 0; width: 100%; top: 258px;
    text-align: center;
    font-family: "Cinzel", serif; font-weight: 700;
    font-size: 30px; letter-spacing: 1px;
    color: var(--card-white);
  }

  /* Back */
  .card-back {
    left: 409px; top: 592px; width: 704px; height: 429px;
    background: linear-gradient(120deg, var(--silver-start) 0%, #e2e6e6 45%, var(--silver-end) 100%);
  }
  .contact-divider {
    position: absolute; left: 154px; top: 98px; width: 1px; height: 244px;
    background: var(--ink-navy);
  }
  .contact {
    position: absolute; left: 183px;
    font-family: "Pathway Gothic One", sans-serif;
    font-size: 17px; line-height: 20px;
  }
  .contact-person { top: 95px; color: var(--ink-navy); }
  .contact-address { top: 181px; color: var(--ink-grey); line-height: 22px; }
  .contact-phone { top: 299px; color: var(--ink-navy); line-height: 23px; }
  .contact-phone .leader { letter-spacing: -1px; }
</style>
</head>
<body>
<main class="canvas">
  <section class="card card-front" aria-label="Card front">
    <div class="brand-rule"></div>
    <h1 class="brand-name">Bright Pathway</h1>
  </section>

  <section class="card card-back" aria-label="Card back">
    <div class="contact-divider"></div>
    <p class="contact contact-person">
      Daniel Hartley - Director<br>
      Brightpathway.com.au<br>
      Daniel@brightpathway.com.au
    </p>
    <p class="contact contact-address">
      Level 14<br>
      Harbourline Tower 3<br>
      88&nbsp;&nbsp;&nbsp;&nbsp;Kent Street<br>
      Harbourside, Sydney 2000
    </p>
    <p class="contact contact-phone">
      Tell <span class="leader">-------------------</span>(02)&nbsp;&nbsp;95550142<br>
      Fax <span class="leader">-------------------</span> (02)&nbsp;&nbsp;95550143
    </p>
  </section>
</main>
</body>
</html>
```